Garden Design Flier

I would like a PDF of this half page A4 flier in soft green tones with dark green leaves.

Target Market(s)

Home owners and real estate agents

Font styles to use
Serif
Other font styles liked:
• Papyrus

Colors
acd136
9bcb3c
cadf82
fefdec

Requirements
Must have
• Green tones
Nice to have
• Leaves, vines, lawns
Should not have
• Open to ideas, but classic style

```html
<!DOCTYPE html>
<html lang="en">
<head>
<meta charset="utf-8">
<title>Parterre Gardens – Flier</title>
<link href="https://fonts.googleapis.com/css2?family=Source+Sans+3:wght@400;600&family=Noto+Sans:wght@700&display=swap" rel="stylesheet">
<style>
  :root {
    --page: #ffffff;
    --paper: #f8faf4;
    --green-deep: #63b245;
    --green-soft: #8dc85e;
    --green-vine: #3db54a;
    --green-icon: #1e8a4a;
    --ink: #000000;
  }
  html, body {
    margin: 0;
    width: 1200px;
    height: 1100px;
    overflow: hidden;
    background: var(--page);
  }
  .flier {
    position: absolute;
    left: 348px;
    top: 153px;
    width: 561px;
    height: 793px;
    background: var(--paper);
    overflow: hidden;
    font-family: "Source Sans 3", sans-serif;
    color: var(--ink);
  }
  .waves {
    position: absolute;
    inset: 0;
    width: 100%;
    height: 100%;
  }
  .vine-art {
    position: absolute;
    border-radius: 50%;
    background: radial-gradient(ellipse at center, rgba(61,181,74,0.28) 0%, rgba(61,181,74,0.12) 55%, rgba(61,181,74,0) 75%);
  }
  .vine-art--top { left: 21px; top: 0; width: 170px; height: 173px; }
  .vine-art--bottom { left: 361px; top: 428px; width: 197px; height: 210px; }
  .brand, .brand-sub, .owner, .credential {
    position: absolute;
    left: 0;
    width: 100%;
    text-align: center;
    margin: 0;
    font-weight: 400;
    line-height: 1;
    box-sizing: border-box;
    padding-left: 8px;
  }
  .brand { top: 157px; font-size: 70px; letter-spacing: 1px; }
  .brand-sub { top: 239px; font-size: 30px; }
  .owner { top: 282px; font-size: 24px; padding-left: 6px; }
  .credential { top: 319px; font-size: 15px; }
  .services {
    position: absolute;
    left: 130px;
    top: 351px;
    width: 318px;
    display: flex;
    justify-content: space-between;
    font-family: "Noto Sans", sans-serif;
    font-weight: 700;
    font-size: 21px;
    line-height: 1;
    margin: 0;
    padding: 0;
    list-style: none;
  }
  .intro {
    position: absolute;
    left: 129px;
    top: 402px;
    width: 300px;
    margin: 0;
    font-size: 12px;
    line-height: 14.8px;
  }
  .contact {
    position: absolute;
    left: 130px;
    top: 479px;
    margin: 0;
    padding: 0;
    list-style: none;
    font-size: 14px;
  }
  .contact li {
    display: flex;
    align-items: center;
    height: 22px;
    margin-bottom: 12px;
  }
  .contact .icon { width: 22px; height: 22px; margin-right: 11px; flex: none; }
  .contact .plain { margin-left: 33px; }
</style>
</head>
<body>
<main class="flier">
  <svg class="waves" viewBox="0 0 943 1333" preserveAspectRatio="none" aria-hidden="true">
    <path fill="var(--green-deep)" d="M0 352 C100 460 160 620 154 800 C145 1000 260 1165 446 1173 C540 1178 610 1120 666 1068 C760 980 860 935 943 915 V1333 H0 Z"/>
    <path fill="var(--green-soft)" d="M0 425 C80 510 115 620 110 720 C105 900 115 1030 230 1135 C290 1195 350 1215 420 1208 C500 1200 580 1165 641 1136 C560 1210 480 1260 400 1260 C300 1260 220 1210 180 1170 C110 1090 90 980 70 820 C55 720 30 660 0 622 Z"/>
    <path fill="var(--green-soft)" d="M943 1005 C860 1025 810 1070 780 1105 C700 1200 600 1290 428 1305 C620 1320 740 1260 800 1200 C850 1150 900 1110 943 1100 Z"/>
  </svg>

  <div class="vine-art vine-art--top" role="img" aria-label="Illustration of a curling green vine with leaves"></div>
  <div class="vine-art vine-art--bottom" role="img" aria-label="Illustration of a curling green vine with leaves"></div>

  <h1 class="brand">PARTERRE</h1>
  <p class="brand-sub">GARDENS</p>
  <p class="owner">by Alex Morgan</p>
  <p class="credential">Certificate 3. Horticulture. Greenfield College</p>

  <ul class="services">
    <li>Design</li>
    <li>Instal</li>
    <li>Grow</li>
    <li>Tend</li>
    <li>Enjoy</li>
  </ul>

  <p class="intro">All your Gardening and landscaping needs from design<br>and installation to general maintenance.<br>Bespoke vegetable gardens and potager designs created<br>to suite your site and requirements.</p>

  <ul class="contact">
    <li>
      <svg class="icon" viewBox="0 0 22 22" aria-hidden="true">
        <circle cx="11" cy="11" r="11" fill="var(--green-icon)"/>
        <g fill="none" stroke="#fff" stroke-width="1.1">
          <circle cx="11" cy="11" r="5.5"/>
          <ellipse cx="11" cy="11" rx="2.4" ry="5.5"/>
          <line x1="5.5" y1="11" x2="16.5" y2="11"/>
          <line x1="6.3" y1="8.2" x2="15.7" y2="8.2"/>
          <line x1="6.3" y1="13.8" x2="15.7" y2="13.8"/>
        </g>
      </svg>
      alex@parterregardens.example
    </li>
    <li>
      <svg class="icon" viewBox="0 0 22 22" aria-hidden="true">
        <path fill="var(--green-icon)" d="M5 2.5 C6 2 7 2.2 7.6 3.2 L9 6 C9.4 6.9 9.1 7.7 8.3 8.2 L7.4 8.8 C8 11.2 10 13.6 12.4 14.8 L13 13.9 C13.6 13.1 14.5 12.9 15.3 13.4 L17.9 15 C18.8 15.6 19 16.6 18.4 17.5 L17.6 18.6 C16.8 19.7 15.4 20 14 19.4 C9 17.2 5 12.8 3.4 7.4 C3 6 3.4 4.4 4.4 3.4 Z"/>
      </svg>
      0400-123456
    </li>
    <li><span class="plain">ABN:12345678901</span></li>
  </ul>
</main>
</body>
</html>
```